Graphic Banner Design - 2.5' x 6' - High Tech Company

We are in need of a banner design for an outdoor sign that will be used at sponsorship events.

Size
2.5' x 6'

The company is a high tech company, and the design will be used for action sports events. So lining up to that would be good.

Tag line to be incorporated...
"Extreme IT Services for Extreme Needs."

Target Market(s)

Business Owners, Entrepreneurs, IT Professionals.

Industry/Entity Type

Information Technology

Logo Text

Brindlex

Colors

Designer to choose colors to be used in the design.

Requirements
Must have
• Must feel young and vibrant, fit in to an action sports event and just be out of this world awesome.
• In the world of the IT, we are the Castavelli. Fast, Awesome, not necessarily cheap, but you know it will do what you want extremely well. Not for everyone, but always desired.

```html
<!DOCTYPE html>
<html lang="en">
<head>
<meta charset="utf-8">
<title>Brindlex – Event Banner Variants</title>
<link href="https://fonts.googleapis.com/css2?family=Montserrat:wght@400;500&display=swap" rel="stylesheet">
<style>
  :root {
    --page-bg: #f7f7f7;
    --navy-deep: #0b0d2a;
    --indigo: #3a3f9e;
    --violet: #6f6fd0;
    --stage-glow: #e9f3ff;
    --cyan-haze: #bfe0f0;
    --ink-dark: #0e0f1c;
    --ink-light: #ffffff;
    --hero-ink: #10124a;
  }
  * { margin: 0; padding: 0; box-sizing: border-box; }
  html, body {
    width: 1200px;
    height: 629px;
    overflow: hidden;
    background: var(--page-bg);
    font-family: "Montserrat", sans-serif;
  }
  .canvas {
    position: relative;
    width: 1200px;
    height: 629px;
  }
  .banner {
    position: absolute;
    left: 38px;
    width: 1122px;
    height: 268px;
    overflow: hidden;
    box-shadow: 0 0 2px rgba(0,0,0,0.15);
  }
  .banner--light { top: 38px; }
  .banner--dark  { top: 322px; }

  .concert-photo {
    position: absolute;
    inset: 0;
    background:
      radial-gradient(ellipse 120px 170px at 460px 40px, var(--stage-glow) 0%, rgba(233,243,255,0) 100%),
      radial-gradient(ellipse 180px 200px at 780px 90px, var(--stage-glow) 0%, rgba(233,243,255,0) 100%),
      radial-gradient(ellipse 160px 180px at 1040px 60px, var(--cyan-haze) 0%, rgba(191,224,240,0) 100%),
      radial-gradient(ellipse 140px 140px at 260px 60px, rgba(200,220,255,0.8) 0%, rgba(200,220,255,0) 100%),
      linear-gradient(180deg, rgba(0,0,0,0) 65%, rgba(20,20,40,0.55) 100%),
      linear-gradient(90deg, var(--navy-deep) 0%, var(--indigo) 25%, var(--violet) 50%, #8fa6dc 75%, var(--cyan-haze) 100%);
  }
  .banner--light .concert-photo { filter: brightness(1.12) saturate(0.85); }
  .banner--light .concert-photo::after {
    content: "";
    position: absolute;
    inset: 0;
    background: rgba(255,255,255,0.12);
  }
  .banner--dark .concert-photo::after {
    content: "";
    position: absolute;
    inset: 0;
    background: linear-gradient(90deg, rgba(0,0,0,0.85) 0%, rgba(0,0,0,0.2) 30%, rgba(0,0,0,0) 55%);
  }

  .brand {
    position: absolute;
    left: 56px;
    top: 37px;
    display: flex;
    align-items: center;
    gap: 34px;
  }
  .brand__mark {
    width: 14px;
    height: 14px;
    border-radius: 50%;
  }
  .brand__name {
    font-size: 26px;
    font-weight: 500;
    letter-spacing: 0.5px;
    line-height: 30px;
  }

  .hero-name {
    position: absolute;
    left: 561px;
    top: 135px;
    transform: translate(-50%, -50%);
    font-size: 72px;
    font-weight: 500;
    letter-spacing: 1px;
    line-height: 1;
    color: var(--hero-ink);
    white-space: nowrap;
  }

  .tagline {
    position: absolute;
    right: 43px;
    bottom: 24px;
    font-size: 19px;
    font-weight: 400;
    line-height: 23px;
    white-space: nowrap;
  }

  .banner--light .brand__name,
  .banner--light .tagline { color: var(--ink-dark); }
  .banner--light .brand__mark { background: var(--ink-dark); }

  .banner--dark .brand__name,
  .banner--dark .tagline { color: var(--ink-light); }
  .banner--dark .brand__mark { background: var(--ink-light); }
</style>
</head>
<body>
<main class="canvas">
  <section class="banner banner--light">
    <div class="concert-photo" role="img" aria-label="Live concert photo: band on a stage under blue and white spotlights with a cheering crowd raising hands in the foreground"></div>
    <div class="brand">
      <span class="brand__mark"></span>
      <span class="brand__name">Brindlex</span>
    </div>
    <p class="hero-name">Brindlex</p>
    <p class="tagline">Extreme IT Services for Extreme Needs</p>
  </section>

  <section class="banner banner--dark">
    <div class="concert-photo" role="img" aria-label="Live concert photo: band on a stage under blue and white spotlights with a cheering crowd raising hands in the foreground"></div>
    <div class="brand">
      <span class="brand__mark"></span>
      <span class="brand__name">Brindlex</span>
    </div>
    <p class="hero-name">Brindlex</p>
    <p class="tagline">Extreme IT Services for Extreme Needs</p>
  </section>
</main>
</body>
</html>
```